Business Card for a new businees.

need a very good business for a new company based in Riverside California call Levy Lantern LLC. We help client file taxes, resolve tax debt and attain peace of mind We help people nationwide solve Tax problems. We help with Installment agreements, Offers in Compromise, Partial Pay Installment Agreements, Currently Not Collectible status, Liens and Levy Removal, Garnishment removal. We offer individualized services

Target Market(s)

Any one with Tax Problems nationwide. My clients span across age, occupation etc

Contact Information for Business Card

Card must be attractive and have enough information to let client know we care and call us

Colors

Designer to choose colors to be used in the design.

Requirements
Must have
• the basics and then surprise me
Nice to have
• surprise m

```html
<!DOCTYPE html>
<html lang="en">
<head>
<meta charset="utf-8">
<title>Levy Lantern LLC — Business Card</title>
<link href="https://fonts.googleapis.com/css2?family=Open+Sans:wght@400;600;700;800&display=swap" rel="stylesheet">
<style>
  :root {
    --canvas: #ece9e2;
    --yellow-light: #f3dd00;
    --yellow: #dcc400;
    --yellow-deep: #c9ae00;
    --gold: #a89016;
    --gold-dark: #857114;
    --ink: #2d2a1e;
    --white: #ffffff;
    --card-w: 630px;
    --card-h: 360px;
  }
  * { box-sizing: border-box; margin: 0; padding: 0; }
  html, body {
    width: 1200px; height: 1200px; overflow: hidden;
    background: var(--canvas);
    font-family: "Open Sans", Arial, sans-serif;
  }
  .sheet {
    width: 1200px; height: 1200px;
    display: flex; flex-direction: column; align-items: center; justify-content: center;
    gap: 80px;
  }
  .card {
    position: relative;
    width: var(--card-w); height: var(--card-h);
    border-radius: 4px; overflow: hidden;
    box-shadow: 0 10px 30px rgba(60, 50, 20, 0.18);
  }

  /* Front */
  .card--front {
    background: linear-gradient(160deg, var(--yellow-deep) 0%, var(--yellow) 45%, var(--yellow-light) 100%);
    color: var(--white);
  }
  .brand {
    position: absolute; left: 50%; top: 50%;
    transform: translate(-50%, -50%);
    display: flex; flex-direction: column; align-items: flex-start;
  }
  .brand__row { display: flex; align-items: center; gap: 16px; }
  .brand__dot {
    width: 38px; height: 38px; border-radius: 50%;
    background: currentColor;
  }
  .brand__name {
    font-weight: 800; font-size: 50px; line-height: 1;
    letter-spacing: -1px; white-space: nowrap;
  }
  .brand__rule {
    width: 100%; height: 3px; background: currentColor; margin: 14px 0 9px;
  }
  .brand__services {
    font-weight: 700; font-size: 11px; letter-spacing: 4px; white-space: nowrap;
  }
  .brand__promise {
    font-weight: 600; font-size: 8.5px; letter-spacing: 0.6px; margin-top: 4px; white-space: nowrap;
  }

  /* Back */
  .card--back { background: var(--white); }
  .card__corner { position: absolute; inset: 0; width: 100%; height: 100%; }
  .card--back .brand {
    left: 250px; top: 38px; transform: none;
    color: var(--gold);
  }
  .card--back .brand__name { font-size: 40px; }
  .card--back .brand__dot { width: 30px; height: 30px; }
  .card--back .brand__services,
  .card--back .brand__promise { color: var(--ink); }
  .card--back .brand__services { font-size: 9px; letter-spacing: 3.4px; }
  .card--back .brand__promise { font-size: 7px; color: var(--gold); }

  .person {
    position: absolute; left: 250px; top: 190px; color: var(--gold);
  }
  .person__name { font-weight: 700; font-size: 26px; line-height: 1.1; }
  .person__role { font-weight: 400; font-size: 15px; color: var(--gold-dark); }

  .contacts {
    position: absolute; left: 250px; bottom: 36px;
    display: grid; grid-template-columns: auto auto; column-gap: 36px; row-gap: 10px;
    color: var(--gold); font-size: 13px; font-weight: 600;
  }
  .contact { display: flex; align-items: center; gap: 8px; white-space: nowrap; }
  .contact svg { width: 14px; height: 14px; fill: var(--gold); flex: none; }
</style>
</head>
<body>
<main class="sheet">

  <section class="card card--front" aria-label="Card front">
    <div class="brand">
      <div class="brand__row">
        <span class="brand__dot"></span>
        <span class="brand__name">Levy Lantern</span>
      </div>
      <span class="brand__rule"></span>
      <span class="brand__services">TAX SOLUTIONS . TAX FILING.</span>
      <span class="brand__promise">YOUR TAX REPRESENTATIVES. WE ARE TAX EVERYTHING</span>
    </div>
  </section>

  <section class="card card--back" aria-label="Card back">
    <svg class="card__corner" viewBox="0 0 630 360" preserveAspectRatio="none" aria-hidden="true">
      <polygon points="0,0 150,0 215,360 0,360" fill="#dcc400"/>
      <polygon points="0,0 120,0 80,360 0,360" fill="#e9d200"/>
      <polygon points="150,0 215,360 190,360 130,0" fill="#a8951a"/>
      <polygon points="215,360 160,360 150,0" fill="#c9ae00"/>
    </svg>

    <div class="brand">
      <div class="brand__row">
        <span class="brand__dot"></span>
        <span class="brand__name">Levy Lantern</span>
      </div>
      <span class="brand__rule"></span>
      <span class="brand__services">TAX SOLUTIONS . TAX FILING.</span>
      <span class="brand__promise">YOUR TAX REPRESENTATIVES. WE ARE TAX EVERYTHING</span>
    </div>

    <div class="person">
      <p class="person__name">Dana Whitfield</p>
      <p class="person__role">Director</p>
    </div>

    <div class="contacts">
      <p class="contact">
        <svg viewBox="0 0 24 24"><path d="M6.6 10.8a15 15 0 0 0 6.6 6.6l2.2-2.2a1 1 0 0 1 1-.25 11.4 11.4 0 0 0 3.6.57 1 1 0 0 1 1 1V20a1 1 0 0 1-1 1A17 17 0 0 1 3 4a1 1 0 0 1 1-1h3.5a1 1 0 0 1 1 1c0 1.25.2 2.45.57 3.57a1 1 0 0 1-.25 1z"/></svg>
        +XXX XX XXX XXX
      </p>
      <p class="contact">
        <svg viewBox="0 0 24 24"><path d="M2 5h20v14H2z M4 7v.4l8 5.2 8-5.2V7z" fill-rule="evenodd"/></svg>
        yourmail@mail.com
      </p>
      <p class="contact">
        <svg viewBox="0 0 24 24"><path d="M7 1h10a2 2 0 0 1 2 2v18a2 2 0 0 1-2 2H7a2 2 0 0 1-2-2V3a2 2 0 0 1 2-2zm0 3v14h10V4zm5 15.5a1.2 1.2 0 1 0 0 2.4 1.2 1.2 0 0 0 0-2.4z"/></svg>
        +XXX XX XXX XXX
      </p>
      <p class="contact">
        <svg viewBox="0 0 24 24"><path d="M12 2a10 10 0 1 0 0 20 10 10 0 0 0 0-20zm6.9 9h-3a15 15 0 0 0-1.3-6 8 8 0 0 1 4.3 6zM12 4.1c.9 1.3 1.7 3.7 1.9 6.9h-3.8c.2-3.2 1-5.6 1.9-6.9zM9.4 5a15 15 0 0 0-1.3 6h-3a8 8 0 0 1 4.3-6zM5.1 13h3a15 15 0 0 0 1.3 6 8 8 0 0 1-4.3-6zm6.9 6.9c-.9-1.3-1.7-3.7-1.9-6.9h3.8c-.2 3.2-1 5.6-1.9 6.9zm2.6-.9a15 15 0 0 0 1.3-6h3a8 8 0 0 1-4.3 6z"/></svg>
        www.yoursite.com
      </p>
    </div>
  </section>

</main>
</body>
</html>
```